Private Practice Dietitian's Business Card

A 2-sided business card for a dietitian (medical nutritionist) in private practice within a natural therapies allied health clinic. The business card needs to imply warmth and professionalism.
Target Market(s)
Doctors who may refer patients to a dietitian and patients themselves who may request dietetic assessment, education and counselling.
Industry/Entity Type
Business
Requirements
Must have
- The business card must be an intense blue on the front at the bottom, gradually lightening towards the top of the card. Please see:
http://example-pinboard.net/remy_hastwell/card-ideas/
for an example from "The quiet of the orchard" book. I'd like an apple tree on the left with a pale silver/grey trunk (like the silver in the book cover)and branches that bends over to the right above the writing. Apples to be a turquoise/aqua colour similar to that in "The quiet of the orchard" book cover. Front cover writing to read:
plateplan
0482 913 276
plateplan@kettlemail.net.au
'plateplan' is one word but I would like the 'my' in turquoise/aqua to match the apples and the 'dietitian' and the phone number and email address in the pale silver/grey to match the tree trunk.
I'd like the plateplan in larger font than the phone number and email address but for all 3 lines of text on the front of the business card to be stretched so they have the same left and right margin. (I hope this makes sense!)
I would like the back of the card to be white and the top section of text to be in the same turquoise/aqua from the apples on the front of the card and to read:
MAREE TOLBIN
Accredited Practising Dietitian (APD)
Bachelor of Health Science (Nutrition & Dietetics) - Honours
Master of Nutrition & Dietetics
This text should be stretched/compacted so that it all has the same left and right margin.
After this text there should be a blank line for spacing before the next section of text, which is to be in the silver/grey of the tree trunk. It should read:
Weight management
Diabetes
Impaired fasting glycaemia
Impaired glucose tolerance
Gestational diabetes
Wellness & general nutrition
Cardiovascular disease
high blood pressure
High cholesterol
High triglycerides
Fatty liver
Constipation
Diverticular disease
Coeliac disease
Irritable bowel syndrome
Gastroesophageal reflux
Lactose intolerance
Gout
Polycystic ovarian syndrome
Fertility
Pregnancy
Breastfeeding
Osteoporosis
Iron deficiency
Vegetarian eating
This set of text can run across the page from left to right and each medical condition could be separated from the next in some way to help with ease of reading. For example perhaps a space, dot and another space could separate the medical conditions. This set of text should be stretched so that the left and right margins of each line is the same. Thank you!
Nice to have
- An easy-to read but 'elegant' font would be nice - but I have no idea which one! Nothing too ornate, but not dull standard Times New Roman/Arial/Comic Sans either!
Should not have
- Times new roman/comic sans/arial fonts

```html
<!DOCTYPE html>
<html lang="en">
<head>
<meta charset="utf-8">
<title>plateplan – Business Card, Front and Back</title>
<link rel="stylesheet" href="https://fonts.googleapis.com/css2?family=Cabin:wght@400;500&family=EB+Garamond:wght@400&display=swap">
<style>
  :root {
    --page: #ffffff;
    --label: #222222;
    --card-top: #dcdde8;
    --card-mid: #8b97bf;
    --card-bottom: #0f4a86;
    --silver: #e4e5ee;
    --trunk-silver: rgba(238, 239, 245, 0.95);
    --trunk-haze: rgba(200, 204, 226, 0.7);
    --leaf-navy: rgba(52, 56, 130, 0.55);
    --apple-aqua: rgba(38, 110, 160, 0.45);
    --navy: #2b2f86;
    --credential-blue: #2c4f9c;
    --condition-grey: #cfcfd3;
    --bullet-grey: #8e8e94;
    --card-edge: #8a8a8a;
  }
  * { margin: 0; padding: 0; box-sizing: border-box; }
  html, body {
    width: 1200px;
    height: 900px;
    overflow: hidden;
    background: var(--page);
  }
  .sheet {
    position: relative;
    width: 1200px;
    height: 900px;
  }
  .side-label {
    position: absolute;
    top: 18px;
    font-family: "Cabin", sans-serif;
    font-size: 17px;
    color: var(--label);
    letter-spacing: 0.02em;
  }
  .side-label--front { left: 116px; }
  .side-label--back { left: 622px; }

  .card {
    position: absolute;
    overflow: hidden;
  }
  .card--front {
    left: 114px;
    top: 44px;
    width: 462px;
    height: 822px;
    background: linear-gradient(to bottom, var(--card-top) 0%, var(--card-mid) 45%, var(--card-bottom) 100%);
  }
  .card--back {
    left: 618px;
    top: 52px;
    width: 468px;
    height: 814px;
    background: var(--page);
    border: 1px solid var(--card-edge);
  }
  .tree-art {
    position: absolute;
    left: 0;
    top: 0;
    width: 462px;
    height: 520px;
    background:
      radial-gradient(ellipse 55% 40% at 72% 38%, var(--apple-aqua) 0%, rgba(38,110,160,0) 100%),
      radial-gradient(ellipse 60% 45% at 38% 30%, var(--trunk-silver) 0%, var(--trunk-haze) 45%, rgba(200,204,226,0) 100%),
      radial-gradient(ellipse 90% 55% at 60% 20%, var(--leaf-navy) 0%, rgba(52,56,130,0) 100%);
    -webkit-mask-image: linear-gradient(to bottom, #000 0%, #000 65%, transparent 100%);
            mask-image: linear-gradient(to bottom, #000 0%, #000 65%, transparent 100%);
  }
  .card svg {
    position: absolute;
    left: 0;
    top: 0;
  }
  .brand-name {
    font-family: "Cabin", sans-serif;
    font-size: 40px;
    fill: var(--silver);
  }
  .contact {
    font-family: "Cabin", sans-serif;
    fill: var(--silver);
  }
  .contact--phone { font-size: 30px; }
  .contact--email { font-size: 27px; }

  .practitioner-name {
    font-family: "Cabin", sans-serif;
    font-weight: 500;
    font-size: 48px;
    fill: var(--navy);
  }
  .credential {
    font-family: "Cabin", sans-serif;
    font-size: 17px;
    fill: var(--credential-blue);
  }
  .conditions {
    font-family: "EB Garamond", serif;
    font-size: 19px;
    fill: var(--condition-grey);
  }
  .conditions .sep { fill: var(--bullet-grey); }
</style>
</head>
<body>
<main class="sheet">
  <span class="side-label side-label--front">FRONT</span>
  <span class="side-label side-label--back">BACK</span>

  <section class="card card--front" aria-label="Card front">
    <div class="tree-art" role="img" aria-label="Illustration of an apple tree with a pale silver trunk bending over to the right, navy leaves and aqua apples"></div>
    <svg width="462" height="822" viewBox="0 0 462 822">
      <text class="brand-name" x="96" y="554" textLength="326" lengthAdjust="spacingAndGlyphs">PLATEPLAN</text>
      <text class="contact contact--phone" x="96" y="608" textLength="326" lengthAdjust="spacing">0482 913 276</text>
      <text class="contact contact--email" x="96" y="646" textLength="326" lengthAdjust="spacingAndGlyphs">plateplan@kettlemail.net.au</text>
    </svg>
  </section>

  <section class="card card--back" aria-label="Card back">
    <svg width="468" height="814" viewBox="0 0 468 814">
      <text class="practitioner-name" x="30" y="198" textLength="402" lengthAdjust="spacingAndGlyphs">MAREE TOLBIN</text>
      <text class="credential" x="30" y="234" textLength="402" lengthAdjust="spacing">Accredited Practising Dietitian (APD)</text>
      <text class="credential" x="30" y="266" textLength="402" lengthAdjust="spacingAndGlyphs">Bachelor of Health Science (Nutrition &amp; Dietetics) - Honours</text>
      <text class="credential" x="30" y="300" textLength="402" lengthAdjust="spacing">Master of Nutrition &amp; Dietetics</text>

      <g class="conditions">
        <text x="30" y="478" textLength="404" lengthAdjust="spacing">Weight management <tspan class="sep">•</tspan> Diabetes <tspan class="sep">•</tspan> Impaired fasting glycaemia</text>
        <text x="30" y="512" textLength="404" lengthAdjust="spacing">Impaired glucose tolerance <tspan class="sep">•</tspan> Gout <tspan class="sep">•</tspan> Gestational diabetes</text>
        <text x="30" y="546" textLength="404" lengthAdjust="spacing">Wellness &amp; general nutrition <tspan class="sep">•</tspan> Cardiovascular disease</text>
        <text x="30" y="580" textLength="404" lengthAdjust="spacing">high blood pressure <tspan class="sep">•</tspan> High cholesterol <tspan class="sep">•</tspan> High triglycerides</text>
        <text x="30" y="614" textLength="404" lengthAdjust="spacing">Fatty liver <tspan class="sep">•</tspan> Diverticular disease <tspan class="sep">•</tspan> Lactose intolerance</text>
        <text x="30" y="648" textLength="404" lengthAdjust="spacing">Coeliac disease Osteoporosis <tspan class="sep">•</tspan> Irritable bowel syndrome</text>
        <text x="30" y="682" textLength="404" lengthAdjust="spacing">Gastroesophageal reflux <tspan class="sep">•</tspan> Polycystic ovarian syndrome</text>
        <text x="30" y="716" textLength="404" lengthAdjust="spacing">Polycystic ovarian syndrome <tspan class="sep">•</tspan> Vegetarian eating <tspan class="sep">•</tspan> Fertility</text>
        <text x="30" y="750" textLength="404" lengthAdjust="spacing">Pregnancy <tspan class="sep">•</tspan> Breastfeeding <tspan class="sep">•</tspan> Iron deficiency Constipation</text>
      </g>
    </svg>
  </section>
</main>
</body>
</html>
```